Norwegian psychologist service needs a fresh and exiting web site*

Norwegian psychologist service: working with therapy, personal development, mastery and personal growth. Focus: children and teenagers with special needs; family dynamics; group processes; individuals with a need for therapy and personal growth. (Our company name: Fjordlys og samhold (means Mastery and Growth).

We already have a logo for the company, which will be used (will be attached in the project).

The webside is to be structured in 4 pages with roll down curtain menus (the numbers are just for guiding the designer - the should not be added):

Page 1: Om Fjordlys og Samhold (about Mastery and Growth): this is where our business is is presented/described shortly: Lorem Ipsum dolor cit...

Page 2: Tjenester (Services): this is where our 5 service areas are presented:
2.1 Utredning (Investigation, diagnosing): Lorem Ipsum dolor cit...
2.2 Rådgivning (consulting): Lorem Ipsum dolor cit...

2.3 Kurs og work shops (courses and work shops): Lorem Ipsum dolor cit...
2.3a Fjordlys og samhold Tema 1 (T1)
2.3b Fjordlys og samhold Tema 2 (T2)
2.3c Fjordlys og samhold Tema 3 (T3)

2.4 Terapi og utvikling (Therapy and development)
2.4a Fjordlys og samhold for individer (FS1)
2.4b Fjordlys og samhold i familier (FS2)
2.4c Fjordlys og samhold i grupper (FS3)
2.4d Fjordlys og samhold i institusjoner (FS4)

Page 3: Aktuelt (Blog): this is our blog where we share knowledge and articles

Page 4: Kontakt (Contact): This is the contact form page. Contact form should constitute:
- Ditt navn (your name)
- E-post (your e-mail)
- Emne (subject)
- Melding (message/description)

Our project should also include suggestion for handheld units (iPhone, iPad).
Updates

We have both been traveling with work for a while, and then unfortunately both of us got sick on return, so we need a few more days to evaluate and choose design. Kind Regards Arvid & Margit

Target Market(s)

Focus on therapy, learning, mastery and growth for children and teenagers with special needs, within the family dynamics, or in a group setting.
OUR MARKETS:
Private market: individuals, families, groups and health industry institutions (with focus on learning, mastery, growth (as well as growing up) and psychiatry for children and teenagers with special difficulties and needs)
Public institutions: Government institutions, state institutions and municipality institutions (e.g. schools, municipality health service, hospitals) that serve the public (families with children and teenagers with special needs, and where learning, mastery, growth (as well as growing up) and potential psychiatry is an issue).

Number of Pages Required

4 page

Font styles to use
Sans Serif

Colors

Designer to choose colors to be used in the design.

Requirements
Must have
• The website must have 4 pages with roll down curtain menus (we have added a PDF with suggested structure, and headings, with sub menus - see attached PDF drawing.
• The web page must also use the added logo file - and make the web page work well with our logo.
• We would like the website to have a modern look and we would like the site to be associated with typical HIGH END TOP QUALITY private health institutions, but with a stronger focus on human beings (hands, faces etc), and not white coats and doctors. We are psychologists in the private market.
• For instance, if photos are being used - we tend to like "warm" almost art-like, "grainy" two-tone (e.g. sepia) photos to illustrate our focus. If designer can find such photos as part of design, it would be interesting to us. We would like a few photos like that integrated in the design.
• We also want a design suggestion for how the web page should look like and behave on handheld units (e.g. iPhone, iPad).
Nice to have
• If designer could find a number of suitable photos that matches the business idea and design requirements (see description above), that could follow website, that would be good.
• It could also be nice to have graphic symbols that denote the different pages/subpages (subjects)....
• HORSES: we sometimes use horses as a "tool" in therapy sessions. The horse is not necessarily used for riding, but for contact, communication and grooming. PHOTOS: we would like the designer to find an opportunity for using a photo reflecting this cooperation between therapist, child, teenager and horse. It is a bit up to the designer to find a way to do this... Since the horse is only a tool, among many other tools, it does not have to be much - but we want to try and see how it will work with a photo that also reflects this part of our business.

```html
<!DOCTYPE html>
<html lang="no">
<head>
<meta charset="utf-8">
<title>Fjordlys og Samhold – Psykolog</title>
<link href="https://fonts.googleapis.com/css2?family=Philosopher:wght@400;700&family=Poppins:wght@400;500;600&family=Oswald:wght@500&display=swap" rel="stylesheet">
<style>
:root{
  --green:#0b6a3a;
  --green-dark:#08552e;
  --heading-green:#1c7a45;
  --navy:#262f6e;
  --cta-blue:#23337f;
  --text:#555;
  --light:#f4f4f4;
  --black:#0b0b0b;
  --white:#fff;
}
*{box-sizing:border-box;margin:0;padding:0}
html,body{width:1200px;height:3840px;overflow:hidden}
body{font-family:'Poppins',sans-serif;color:var(--text);background:var(--white);position:relative}
h1,h2,h3,h4{font-family:'Philosopher',sans-serif;font-weight:700}
.btn{display:inline-block;background:var(--navy);color:var(--white);font-family:'Philosopher',sans-serif;font-weight:700;font-size:22px;padding:14px 34px;border-radius:4px}
.photo{display:block}

/* header */
.site-header{position:absolute;top:0;left:0;width:1200px;height:160px;background:var(--white)}
.topbar{position:absolute;right:0;top:0;width:460px;height:36px;background:var(--green);color:var(--white);font-size:15px;display:flex;gap:40px;align-items:center;padding-left:140px}
.topbar span{display:flex;align-items:center;gap:8px}
.brand{position:absolute;left:70px;top:40px;display:flex;align-items:center;gap:14px}
.brand-mark{width:52px;height:52px;border-radius:50%;background:var(--green)}
.brand-name{font-family:'Poppins',sans-serif;font-weight:600;font-size:22px;color:var(--green)}
.main-nav{position:absolute;right:70px;top:66px;display:flex;gap:34px;font-size:17px;color:#333}

/* hero */
.hero{position:absolute;top:160px;left:0;width:1200px;height:520px;background:linear-gradient(110deg,#8a7f78 0%,#5f5650 40%,#7c716a 70%,#b5aca4 100%)}
.hero-content{position:absolute;left:0;right:0;top:170px;text-align:center;color:var(--white)}
.hero-title{font-family:'Oswald',sans-serif;font-weight:500;font-size:50px;letter-spacing:1px}
.hero-text{font-size:17px;width:580px;margin:10px auto 22px;line-height:1.5}
.slider-arrow{position:absolute;top:222px;width:52px;height:52px;border-radius:50%;background:rgba(255,255,255,.35)}
.slider-arrow.prev{left:10px}.slider-arrow.next{right:10px}
.slider-arrow svg{width:52px;height:52px}

/* about */
.about{position:absolute;top:680px;left:0;width:1200px;height:520px}
.about-text{position:absolute;left:140px;top:70px;width:480px}
.section-title{color:var(--heading-green);font-size:50px;line-height:1.1}
.rule{width:70px;height:3px;background:var(--green);margin:12px 0 24px}
.about-text p{font-size:16px;line-height:1.65;margin-bottom:16px}
.about-photo-main{position:absolute;left:760px;top:50px;width:320px;height:340px;background:linear-gradient(160deg,#f0c9a8,#d49a6e 60%,#a8744e)}
.about-photo-small{position:absolute;left:700px;top:240px;width:200px;height:200px;border:6px solid var(--white);background:linear-gradient(180deg,#d9c39a,#9b7b4a 60%,#4d4a3a)}

/* services */
.services{position:absolute;top:1200px;left:0;width:1200px;height:610px;display:grid;grid-template-columns:repeat(4,300px);grid-template-rows:300px 300px;gap:4px 0}
.service-card{background:var(--green);color:var(--white);padding:46px 36px}
.service-card h3{font-size:32px}
.service-card .rule{background:var(--white);margin:10px 0 18px;width:60px}
.service-card p{font-size:15px;line-height:1.6}
.service-card .more{font-size:13px;font-weight:600;margin-top:18px;display:block}
.ph-a{background:linear-gradient(180deg,#d8d6d2,#a8a49f 60%,#5a5d66)}
.ph-b{background:linear-gradient(160deg,#c6a888,#8a6448 60%,#4e3a2e)}
.ph-c{background:linear-gradient(170deg,#eaeaea,#b8c3cf 50%,#c9a944)}
.ph-d{background:linear-gradient(160deg,#e4e2de,#c39c88 50%,#7b5a4a)}

/* call to action */
.cta{position:absolute;top:1820px;left:0;width:1200px;height:480px}
.cta-text{position:absolute;left:195px;top:95px;width:520px}
.cta-text h2{color:var(--cta-blue);font-size:48px;line-height:1.15}
.cta-text p{font-size:16px;line-height:1.65;margin-bottom:24px}
.cta-photo{position:absolute;left:700px;top:60px;width:370px;height:410px;background:radial-gradient(ellipse at 50% 30%,#e6d3c4 0%,#cfd7dc 45%,#f4f4f4 75%)}

/* contact */
.contact{position:absolute;top:2300px;left:0;width:1200px;height:500px;background:linear-gradient(135deg,#0e6b3b,#1d7a48 40%,#3e7f5a 60%,#0d6a39);color:var(--white);text-align:center}
.contact h2{font-size:48px;padding-top:42px}
.contact .sub{font-size:16px;margin-top:4px}
.contact-form{position:absolute;left:180px;top:155px;width:840px}
.field-row{display:grid;grid-template-columns:repeat(3,1fr);gap:20px;margin-bottom:22px}
.field{height:50px;background:rgba(255,255,255,.25);border:1px solid rgba(255,255,255,.55);text-align:left;padding:14px 16px;font-size:14px;color:var(--white)}
.field.message{height:124px}
.contact .btn{margin-top:26px;font-size:22px;padding:12px 30px}

/* news */
.news{position:absolute;top:2800px;left:0;width:1200px;height:640px;text-align:center}
.news .section-title{padding-top:44px;font-size:52px}
.news .rule{margin:12px auto 40px}
.news-grid{position:absolute;left:120px;top:140px;width:960px;display:grid;grid-template-columns:repeat(3,1fr);gap:30px;text-align:left}
.news-card{background:var(--white);box-shadow:0 2px 10px rgba(0,0,0,.12);height:450px}
.news-card .photo{height:210px}
.news-body{padding:24px 22px}
.news-body h4{font-family:'Poppins',sans-serif;font-weight:600;font-size:15px;color:#222}
.news-date{color:var(--green);font-size:14px;margin:6px 0 16px}
.news-body p{font-size:14px;line-height:1.6}
.news-body .more{display:block;margin-top:14px;font-size:14px;font-weight:600;color:var(--navy)}
.n1{background:linear-gradient(160deg,#b9a27a,#7b7052 60%,#3f4a38)}
.n2{background:linear-gradient(160deg,#cfd9e2,#8ea2b5 55%,#4b5e72)}
.n3{background:linear-gradient(160deg,#eef0ee,#c5c7bf 55%,#8d6d58)}

/* newsletter */
.newsletter{position:absolute;top:3460px;left:0;width:1200px;height:100px;background:var(--green);display:flex;align-items:center;padding-left:90px;gap:90px}
.newsletter h3{color:var(--white);font-family:'Poppins',sans-serif;font-weight:600;font-size:30px}
.newsletter-field{width:380px;height:50px;border:1px solid rgba(255,255,255,.7);display:flex;align-items:center;justify-content:space-between;padding-left:16px;color:var(--white);font-size:14px}
.newsletter-field span.send{width:50px;height:50px;display:flex;align-items:center;justify-content:center}

/* footer */
.site-footer{position:absolute;top:3560px;left:0;width:1200px;height:280px;background:var(--black);color:#ddd}
.footer-brand{position:absolute;left:80px;top:30px;display:flex;align-items:center;gap:12px}
.footer-brand .brand-name{color:var(--white);font-size:20px}
.social{position:absolute;left:80px;top:150px;display:flex;gap:12px}
.social span{width:40px;height:40px;border-radius:50%;background:#3d5a98}
.social span:nth-child(2){background:#1da1f2}.social span:nth-child(3){background:#d42a22}.social span:nth-child(4){background:#dd4b39}
.copyright{position:absolute;left:80px;top:222px;font-size:14px}
.copyright b{color:var(--green);font-weight:500;filter:brightness(1.6)}
.footer-col{position:absolute;top:40px}
.footer-col h4{font-family:'Poppins',sans-serif;font-weight:600;font-size:20px;color:var(--white);margin-bottom:16px}
.footer-col li{list-style:none;font-size:15px;margin-bottom:12px}
.footer-col li::before{content:"›";margin-right:10px}
.footer-col.sitemap{left:690px}.footer-col.contact-info{left:890px}
.footer-col.contact-info li::before{content:none}
.footer-col.contact-info li{display:flex;align-items:center;gap:10px;margin-bottom:20px}
</style>
</head>
<body>

<header class="site-header">
  <div class="topbar">
    <span><svg width="16" height="12" viewBox="0 0 16 12"><rect x="0.5" y="0.5" width="15" height="11" fill="none" stroke="#fff"/><path d="M1 1l7 6 7-6" fill="none" stroke="#fff"/></svg>post@fjordlys.no</span>
    <span><svg width="14" height="14" viewBox="0 0 24 24"><path d="M6.6 10.8a15 15 0 006.6 6.6l2.2-2.2a1 1 0 011-.25 11 11 0 003.5.55 1 1 0 011 1V20a1 1 0 01-1 1A17 17 0 013 4a1 1 0 011-1h3.5a1 1 0 011 1 11 11 0 00.55 3.5 1 1 0 01-.25 1z" fill="#fff"/></svg>22 40 18 60</span>
  </div>
  <div class="brand"><span class="brand-mark"></span><span class="brand-name">Fjordlys og Samhold</span></div>
  <nav class="main-nav"><span>Om Fjordlys og Samhold</span><span>Tjenester</span><span>Aktuelt</span><span>Kontakt</span></nav>
</header>

<section class="hero" role="img" aria-label="Varmt fotografi av en forelder som holder et barn">
  <span class="slider-arrow prev"><svg viewBox="0 0 52 52"><path d="M30 17l-9 9 9 9" fill="none" stroke="#fff" stroke-width="3"/></svg></span>
  <span class="slider-arrow next"><svg viewBox="0 0 52 52"><path d="M22 17l9 9-9 9" fill="none" stroke="#fff" stroke-width="3"/></svg></span>
  <div class="hero-content">
    <h1 class="hero-title">PSYKOLOG MASTERY THERAPY</h1>
    <p class="hero-text">Lorem Ipsum is simply dummy text of the printing and typesetting industry. Lorem Ipsum has been the industry.</p>
    <span class="btn">Avtale et Møte</span>
  </div>
</section>

<section class="about">
  <div class="about-text">
    <h2 class="section-title">Om Fjordlys og Samhold</h2>
    <div class="rule"></div>
    <p>Lorem Ipsum is simply dummy text of the printing and typesetting industry. Lorem Ipsum has been the industry's standard dummy.</p>
    <p>Lorem Ipsum is simply dummy text of the printing and typesetting industry. Lorem Ipsum has been the industry's standard dummy text ever since the 1500s, when an unknown printer took a galley of type and scrambled it to make a type specimen book it.</p>
    <span class="btn">Les mer</span>
  </div>
  <div class="photo about-photo-main" role="img" aria-label="Portrett av et smilende barn"></div>
  <div class="photo about-photo-small" role="img" aria-label="Silhuett med løftede armer i solnedgang"></div>
</section>

<section class="services">
  <div class="photo ph-a" role="img" aria-label="Ungdom som sitter alene på gulvet"></div>
  <article class="service-card"><h3>Utredning</h3><div class="rule"></div><p>Lorem Ipsum is simply dummy text of the printing and type setting industry.</p><span class="more">Learn More ▸</span></article>
  <div class="photo ph-b" role="img" aria-label="Portrett av en ung kvinne"></div>
  <article class="service-card"><h3>Rådgivning</h3><div class="rule"></div><p>Lorem Ipsum is simply dummy text of the printing and type setting industry.</p><span class="more">Learn More ▸</span></article>
  <article class="service-card"><h3>Kurs og work shops</h3><div class="rule"></div><p>Lorem Ipsum is simply dummy text of the printing and type setting industry.</p><span class="more">Learn More ▸</span></article>
  <div class="photo ph-c" role="img" aria-label="Terapeut og barn i samtale i et lyst rom"></div>
  <article class="service-card"><h3>Utredning</h3><div class="rule"></div><p>Lorem Ipsum is simply dummy text of the printing and type setting industry.</p><span class="more">Learn More ▸</span></article>
  <div class="photo ph-d" role="img" aria-label="Mor og barn som leker sammen"></div>
</section>

<section class="cta">
  <div class="cta-text">
    <h2>Hvis du har spørsmål til oss i dag!</h2>
    <div class="rule"></div>
    <p>Lorem Ipsum is simply dummy text of the printing and typesetting industry. Lorem Ipsum has been the industry's standard dummy.</p>
    <span class="btn">Avtale et Møte</span>
  </div>
  <div class="photo cta-photo" role="img" aria-label="Smilende psykolog med en skriveplate"></div>
</section>

<section class="contact" role="img" aria-label="Kontaktseksjon over et grønntonet bilde av en familie">
  <h2>Kontakt Oss</h2>
  <p class="sub">Hvis du har spørsmål til oss i dag!</p>
  <div class="contact-form">
    <div class="field-row"><div class="field">Ditt navn</div><div class="field">E-post</div><div class="field">Emne</div></div>
    <div class="field message">Melding</div>
    <span class="btn">Sende Inn</span>
  </div>
</section>

<section class="news">
  <h2 class="section-title">Siste Aktuelt</h2>
  <div class="rule"></div>
  <div class="news-grid">
    <article class="news-card"><div class="photo n1" role="img" aria-label="Forelder og barn som leser sammen"></div><div class="news-body"><h4>LOREM IPSUM IS TEXT PRINT</h4><div class="news-date">08 Jan 2020</div><p>Lorem Ipsum is simply dummy text of the printing &amp; typesetting simple industry ipsum text.</p><span class="more">Read More ›</span></div></article>
    <article class="news-card"><div class="photo n2" role="img" aria-label="Terapeut i samtale med en ungdom"></div><div class="news-body"><h4>LOREM IPSUM IS TEXT PRINT</h4><div class="news-date">08 Jan 2020</div><p>Lorem Ipsum is simply dummy text of the printing &amp; typesetting simple industry ipsum text.</p><span class="more">Read More ›</span></div></article>
    <article class="news-card"><div class="photo n3" role="img" aria-label="Psykolog og pasient i et lyst kontor"></div><div class="news-body"><h4>LOREM IPSUM IS TEXT PRINT</h4><div class="news-date">08 Jan 2020</div><p>Lorem Ipsum is simply dummy text of the printing &amp; typesetting simple industry ipsum text.</p><span class="more">Read More ›</span></div></article>
  </div>
</section>

<section class="newsletter">
  <h3>Registrer deg for å få nyhetsbrev !</h3>
  <div class="newsletter-field">E-post<span class="send"><svg width="20" height="20" viewBox="0 0 24 24"><path d="M2 21l21-9L2 3v7l15 2-15 2z" fill="#fff"/></svg></span></div>
</section>

<footer class="site-footer">
  <div class="footer-brand"><span class="brand-mark"></span><span class="brand-name">Fjordlys og Samhold</span></div>
  <div class="social"><span></span><span></span><span></span><span></span></div>
  <p class="copyright">© <b>Fjordlys og Samhold</b> - 2020. Alle rettigheter forbeholdt</p>
  <div class="footer-col sitemap"><h4>Sitemap</h4><ul><li>Om Fjordlys og Samhold</li><li>Tjenester</li><li>Aktuelt</li><li>Kontakt</li></ul></div>
  <div class="footer-col contact-info"><h4>Kontakt Oss</h4><ul>
    <li><svg width="16" height="16" viewBox="0 0 24 24"><path d="M6.6 10.8a15 15 0 006.6 6.6l2.2-2.2a1 1 0 011-.25 11 11 0 003.5.55 1 1 0 011 1V20a1 1 0 01-1 1A17 17 0 013 4a1 1 0 011-1h3.5a1 1 0 011 1 11 11 0 00.55 3.5 1 1 0 01-.25 1z" fill="#2e9a5c"/></svg>22 40 18 60</li>
    <li><svg width="18" height="14" viewBox="0 0 16 12"><rect x="0.5" y="0.5" width="15" height="11" fill="none" stroke="#2e9a5c"/><path d="M1 1l7 6 7-6" fill="none" stroke="#2e9a5c"/></svg>post@fjordlys.no</li>
  </ul></div>
</footer>

</body>
</html>
```